Corbett Architecture (business card)

We need a business card design. We are a full service architectural firm that specializes in mostly residential projects and some commercial projects. We are located in Hudson Valley, New York. We work with high end clients and want a business card that is memorable and has a sleek, modern, design but will not go out of style (timeless).

Target Market(s)

high end residential clients

Industry/Entity Type

Architect

Contact Information for Business Card

Front of card
Company Logo
website: www.corbettdesignstudo.example
what we do: residential, Commercial

back of card
Owner's Name: Martin Corbett
owner's title: Principal
Business address: 2867 Orchard Lane Suite B, Maplethorpe, NY 10938
phone number: 845-555-0192
e-mail: mc@corbettdesignstudio.example

We like:
icons
sleek and clean design
simple not too busy or too much text

Font styles to use
Sans Serif

Colors
0356a4

Requirements
Must have
• company colors are navy blue, white, and gray
• Front of card
• Company Logo
• website: www.corbettdesignstudo.example
• what we do: residential, Commercial
• back of card
• Owner's Name: Martin Corbett
• owner's title: Principal
• Business address: 2867 Orchard Lane Suite B, Maplethorpe, NY 10938
• phone number: 845-555-0192
• e-mail: mc@corbettdesignstudio.example
Nice to have
• We like:
• icons
• sleek and clean design
• simple not too much text
• color of the card to be either blue or gray
Should not have
• we do not like houses in the design or plans of houses-this is over done and we don't like it.
• no QR CODES

```html
<!DOCTYPE html>
<html lang="en">
<head>
<meta charset="utf-8">
<title>Corbett Architecture — Business Card</title>
<link rel="stylesheet" href="https://fonts.googleapis.com/css2?family=Josefin+Sans:wght@300;400&family=Montserrat:wght@700&family=Quicksand:wght@400;500&display=swap">
<style>
  :root {
    --navy: #0b0f7a;
    --navy-deep: #040866;
    --navy-bright: #0a0f98;
    --gray: #6e6e75;
    --gray-light: #8a8a90;
    --white: #ffffff;
    --backdrop: #e3e3e3;
  }
  * { margin: 0; padding: 0; box-sizing: border-box; }
  html, body {
    width: 1200px; height: 1200px; overflow: hidden;
    background: var(--backdrop);
  }
  .sheet {
    width: 1200px; height: 1200px;
    display: flex; flex-direction: column; align-items: center; justify-content: center;
    gap: 44px;
  }
  .card {
    width: 900px; height: 514px; position: relative;
    box-shadow: 0 10px 30px rgba(0,0,0,0.12);
  }

  /* Back: contact side */
  .card--contact { background: var(--white); }
  .brand {
    font-family: "Josefin Sans", sans-serif; font-weight: 300;
    display: flex; align-items: center; gap: 14px;
  }
  .brand__square { display: block; background: var(--navy); }
  .brand__name { line-height: 0.95; text-transform: uppercase; }
  .brand__suffix { text-transform: lowercase; }

  .card--contact .brand { position: absolute; left: 52px; top: 60px; color: var(--navy); }
  .card--contact .brand__square { width: 40px; height: 40px; }
  .card--contact .brand__name { font-size: 34px; }
  .card--contact .brand__suffix { font-size: 15px; }

  .person { position: absolute; left: 62px; top: 262px; text-align: right; width: 370px; }
  .person__name {
    font-family: "Montserrat", sans-serif; font-weight: 700; font-size: 31px;
    color: var(--navy); letter-spacing: 0.5px; text-transform: uppercase;
  }
  .person__title {
    font-family: "Quicksand", sans-serif; font-weight: 500; font-size: 13px;
    color: var(--gray); letter-spacing: 8px; text-transform: uppercase;
    margin-top: 2px; margin-right: 100px;
  }

  .contact-rule {
    position: absolute; left: 466px; top: 230px; width: 2px; height: 176px;
    background: var(--navy);
  }
  .contact-list {
    position: absolute; left: 490px; top: 226px; list-style: none;
    font-family: "Quicksand", sans-serif; font-weight: 500; font-size: 15px;
    color: var(--gray);
  }
  .contact-list li { display: flex; align-items: center; gap: 18px; height: 44px; }
  .contact-list svg { width: 24px; height: 24px; fill: var(--navy); flex: none; }

  /* Front: brand side */
  .card--brand {
    background: linear-gradient(100deg, var(--navy-deep) 0%, var(--navy-bright) 55%, var(--navy) 100%);
    color: var(--white);
  }
  .card--brand .brand { position: absolute; left: 180px; top: 150px; gap: 26px; }
  .card--brand .brand__square { width: 74px; height: 74px; background: var(--white); }
  .card--brand .brand__name { font-size: 62px; }
  .card--brand .brand__suffix { font-size: 24px; }

  .services {
    position: absolute; left: 0; right: 0; top: 372px; text-align: center;
    font-family: "Josefin Sans", sans-serif; font-weight: 400; color: var(--white);
  }
  .services__list { font-size: 28px; letter-spacing: 1px; text-transform: uppercase; word-spacing: 6px; }
  .services__web { font-family: "Quicksand", sans-serif; font-weight: 500; font-size: 19px; margin-top: 4px; }
</style>
</head>
<body>
<main class="sheet">

  <section class="card card--contact" aria-label="Business card, contact side">
    <div class="brand">
      <span class="brand__square"></span>
      <div class="brand__name">Corbett<br>Architecture <span class="brand__suffix">pllc</span></div>
    </div>

    <div class="person">
      <h1 class="person__name">Martin Corbett</h1>
      <p class="person__title">Principal</p>
    </div>

    <div class="contact-rule"></div>
    <ul class="contact-list">
      <li>
        <svg viewBox="0 0 24 24" aria-hidden="true"><path d="M12 1.5a7.5 7.5 0 0 0-7.5 7.5c0 5.6 7.5 13.5 7.5 13.5s7.5-7.9 7.5-13.5A7.5 7.5 0 0 0 12 1.5zm0 10.5a3 3 0 1 1 0-6 3 3 0 0 1 0 6z"/></svg>
        <span>2867 Orchard Lane Suite B, Maplethorpe, NY 10938</span>
      </li>
      <li>
        <svg viewBox="0 0 24 24" aria-hidden="true"><path d="M6.6 10.8a15.1 15.1 0 0 0 6.6 6.6l2.2-2.2a1 1 0 0 1 1-.25 11.4 11.4 0 0 0 3.6.57 1 1 0 0 1 1 1V20a1 1 0 0 1-1 1A17 17 0 0 1 3 4a1 1 0 0 1 1-1h3.5a1 1 0 0 1 1 1c0 1.25.2 2.45.57 3.57a1 1 0 0 1-.25 1z"/></svg>
        <span>845-555-0192</span>
      </li>
      <li>
        <svg viewBox="0 0 24 24" aria-hidden="true"><path d="M2 5h20v14H2z M2 5l10 8 10-8" /><path d="M2 6.5l10 7.5 10-7.5V5H2z" fill="#fff" opacity="0.25"/></svg>
        <span>mc@corbettdesignstudio.example</span>
      </li>
      <li>
        <svg viewBox="0 0 24 24" aria-hidden="true"><path d="M4 2l15 9-6.5 1.5 4 7-2.6 1.5-4-7L5 18z"/></svg>
        <span>www.corbettdesignstudo.example</span>
      </li>
    </ul>
  </section>

  <section class="card card--brand" aria-label="Business card, brand side">
    <div class="brand">
      <span class="brand__square"></span>
      <div class="brand__name">Corbett<br>Architecture <span class="brand__suffix">pllc</span></div>
    </div>
    <div class="services">
      <p class="services__list">Residential - Commercial</p>
      <p class="services__web">www.corbettdesignstudo.example</p>
    </div>
  </section>

</main>
</body>
</html>
```